Bright Path Flyer Design for Virtual Online Clinic. -5.5 x 8.5 inches (half sheet)

We need a clean, modern flyer design for Bright Path, a new virtual walk-in clinic based in British Columbia. The flyer will be used in libraries, pharmacies, and community centers to help residents easily access primary care through their Bright Path NFC access card.
The flyer will ask a question : NEED A DOCTOR? This should be large and attention grabbing.
The design should clearly feature a Bright Path card image (the access card) as the centerpiece and visually show how patients can use it to book appointments. The tone should feel trustworthy, healthcare-oriented, and community-friendly — clean fonts, clear spacing, and strong readability from a distance.

Side One: This card has the NFC Access Card.
NEED A DOCTOR? (Large Font, Attention Grabbing)
How to Book an Appointment using your Bright Path Card
Step 1: Tap Your Card on Your Phone
Hold your card near the back of your phone.
It will activate automatically — no app needed.
The Bright Path scheduler will open.
Step 2: Schedule Your Appointment
Select your clinical concern.
Choose your time window.
Register (only once).
Confirm your appointment.
Step 3: Relax, we’ll take care of the rest
A doctor will call during your scheduled time.
Once booked, you’ll be able to call our office.
No emails, no texts — just a real person.
It’s that simple.
Side Two:
About Bright Path
Created by Dr. Marcus Ferrigan
Bright Path was founded to make healthcare simple and convenient. Prescription renewals. Common infections. Medical notes. And so much more.
Our doctors can address 120+ health concerns virtually — providing quality care without the waiting room. No waiting rooms. Just real doctors providing real care.
Why Patients Choose Bright Path
Easy access – book and be seen from anywhere in BC.
Effortless booking – tap your Bright Path Card to begin.
Trusted physicians – every visit is with a licensed BC family doctor.
How It Works
Book your visit — choose a time window that fits your day.
Join the queue — you’ll be called when it’s your turn.
Speak directly with your doctor — simple, secure, and stress-free.
Convenient Care for Common Concerns

Additional Details.
Please find the domain to be launched soon. I've attached the NFC card file for review, it is 85.5 mm x 54 mm. The card will be glued to the flyer.
I've attached examples of flyers but they are not the look I am seeking and I am looking for creative solutions.
Thank you!
http://brightpath-example.test/

Adult Patients in British Columbia

Healthcare

• Looking for clean lines, uniform appearance, and high legibility i.e poppins

0054AA
0677BA
7BADD7
CADEEF
E8F1F8

• Need A Doctor?
• Elegant style, not too busy, clear layout.
• Clutter, look cheap - review examples.

```html
<!DOCTYPE html>
<html lang="en">
<head>
<meta charset="utf-8">
<title>Bright Path – Flyer, Two Sides</title>
<link rel="stylesheet" href="https://fonts.googleapis.com/css2?family=Poppins:ital,wght@0,300;0,400;0,500;0,600;0,700;0,800;1,500;1,700&family=Allura&display=swap">
<style>
  :root{
    --primary:#0054AA;
    --accent:#0677BA;
    --sky:#7BADD7;
    --mist:#CADEEF;
    --pale:#E8F1F8;
    --white:#ffffff;
  }
  *{margin:0;padding:0;box-sizing:border-box}
  html,body{width:1200px;height:876px;overflow:hidden}
  body{background:var(--primary);font-family:"Poppins",sans-serif;color:var(--primary);position:relative}
  .flyer{position:absolute;top:133px;width:464px;height:657px;overflow:hidden;outline:1px solid rgba(255,255,255,.75)}
  .flyer--front{left:96px;background:var(--primary)}
  .flyer--back{left:641px;background:var(--pale)}
  .flyer__shapes{position:absolute;inset:0;width:464px;height:657px}
  .abs{position:absolute}

  /* side one */
  .brand{left:24px;top:58px;color:var(--white);font-weight:600;font-size:16px;letter-spacing:.2px;display:flex;align-items:center;gap:5px}
  .brand__dot{width:7px;height:7px;border-radius:50%;background:var(--sky)}
  .brand__web{left:50px;top:86px;color:var(--white);font-size:5px;letter-spacing:.2px}
  .card-slot{left:138px;top:28px;width:188px;height:118px;background:var(--white);border-radius:7px}
  .doctor-photo{left:300px;top:20px;width:164px;height:268px;background:linear-gradient(180deg,#f3f7fb 0%,var(--pale) 55%,var(--mist) 100%);border-radius:80px 80px 0 0}
  .headline{left:31px;top:182px;width:265px}
  .headline__ask{color:var(--primary);font-weight:800;font-size:26px;line-height:30px;letter-spacing:-.3px}
  .headline__how{color:var(--primary);font-weight:700;font-size:15px;line-height:18px;margin-top:10px}
  .headline__card{color:var(--accent);font-weight:700;font-size:15px;line-height:18px;margin-top:4px}
  .step{position:absolute;text-align:center;color:var(--primary)}
  .step__label{font-weight:700;line-height:1}
  .step__num{font-weight:700;line-height:.9}
  .col-rule{position:absolute;top:452px;width:1px;height:173px;background:rgba(255,255,255,.8)}
  .item{position:absolute;display:flex;gap:9px;color:var(--white);font-size:9.4px;line-height:11.3px;font-weight:400;letter-spacing:.15px}
  .item svg{flex:0 0 17px;width:17px;height:17px;margin-top:1px}
  .tagline{font-family:"Allura",cursive;color:var(--primary);font-size:17px;left:350px;top:628px}

  /* side two */
  .about{left:0;width:464px;top:36px;text-align:center;font-weight:800;font-size:23px;color:var(--primary);letter-spacing:.2px}
  .about__name{font-weight:600}
  .creator{left:0;width:464px;top:67px;text-align:center;font-style:italic;font-weight:500;font-size:8.6px;color:var(--primary)}
  .creator b{font-weight:700}
  .intro{left:0;width:464px;top:91px;text-align:center;font-weight:400;font-size:9.7px;line-height:14px;color:var(--primary)}
  .reach{left:0;width:464px;top:258px;text-align:center;font-size:11.4px;line-height:22px;color:var(--primary)}
  .reach__big{color:var(--accent);font-weight:800;font-size:26px;letter-spacing:-.5px;vertical-align:-3px}
  .promise{left:0;width:464px;top:318px;text-align:center;font-weight:700;font-size:10.6px;color:var(--primary)}
  .promise__accent{color:var(--accent)}
  .benefits{position:absolute;left:21px;top:358px;width:422px;border-collapse:collapse;color:var(--primary);font-size:11.6px;line-height:14px;text-align:center;font-weight:400}
  .benefits th{background:var(--primary);color:var(--white);font-weight:700;font-size:11.4px;line-height:14px;height:43px;border-right:1px solid var(--white)}
  .benefits th:last-child{border-right:0}
  .benefits td{border-bottom:1px solid var(--primary);padding:0 2px}
  .benefits td.left{border-right:1px solid var(--primary);width:211px}
  .r1{height:35px}.r2{height:34px}.r3{height:25px}.r4{height:44px}.r5{height:27px}.r6{height:42px}
  .closing{font-family:"Allura",cursive;color:var(--primary);font-size:17px;left:40px;top:628px}
  .thanks{right:20px;top:622px;text-align:right;color:var(--white)}
  .thanks__title{font-weight:800;font-size:14px;line-height:16px}
  .thanks__url{font-size:8.8px;line-height:11px}
</style>
</head>
<body>

<section class="flyer flyer--front">
  <svg class="flyer__shapes" viewBox="0 0 464 657" aria-hidden="true">
    <path fill="var(--sky)" d="M0,165 C120,95 300,70 464,0 L464,200 C420,330 260,430 0,450 Z"/>
    <path fill="var(--accent)" d="M0,185 C130,110 300,82 464,14 L464,140 C420,300 260,362 0,372 Z"/>
    <path fill="var(--pale)" d="M0,185 C130,110 300,82 464,14 L464,120 C420,280 260,335 0,345 Z"/>
    <path fill="var(--sky)" d="M305,80 C380,64 428,36 450,0 L464,0 L464,6 C440,48 390,76 305,80 Z"/>
    <path fill="var(--sky)" d="M228,657 C330,640 420,610 464,560 L464,657 Z"/>
  </svg>

  <div class="abs brand"><span>Bright Path</span><span class="brand__dot"></span></div>
  <div class="abs brand__web">www.brightpath-example.test</div>

  <div class="abs doctor-photo" role="img" aria-label="Photo of a smiling doctor in a white coat with a stethoscope, arms crossed"></div>
  <div class="abs card-slot" aria-label="Space for the Bright Path access card"></div>

  <h1 class="abs headline">
    <div class="headline__ask">NEED A DOCTOR?</div>
    <div class="headline__how">HOW TO BOOK AN APPOINTMENT</div>
    <div class="headline__card">USING YOUR BRIGHT PATH CARD</div>
  </h1>

  <svg class="flyer__shapes" viewBox="0 0 464 657" aria-hidden="true">
    <path fill="var(--white)" d="M76,395 a33,33 0 0 1 17,61 l-17,14 -17,-14 a33,33 0 0 1 17,-61 Z"/>
    <path fill="var(--white)" d="M229,374 a38,38 0 0 1 20,70 l-20,14 -20,-14 a38,38 0 0 1 20,-70 Z"/>
    <path fill="var(--white)" d="M373,314 a42,42 0 0 1 22,78 l-22,15 -22,-15 a42,42 0 0 1 22,-78 Z"/>
  </svg>
  <div class="step" style="left:46px;top:408px;width:60px">
    <div class="step__label" style="font-size:12px">STEP</div>
    <div class="step__num" style="font-size:29px">01</div>
  </div>
  <div class="step" style="left:194px;top:386px;width:70px">
    <div class="step__label" style="font-size:14px">STEP</div>
    <div class="step__num" style="font-size:36px">02</div>
  </div>
  <div class="step" style="left:333px;top:328px;width:80px">
    <div class="step__label" style="font-size:15px">STEP</div>
    <div class="step__num" style="font-size:39px">03</div>
  </div>

  <div class="col-rule" style="left:158px"></div>
  <div class="col-rule" style="left:305px"></div>

  <div class="item" style="left:17px;top:473px"><svg viewBox="0 0 17 17" fill="none" stroke="#fff" stroke-width="1"><rect x="1" y="2" width="10" height="13" rx="1.5"/><rect x="6" y="6" width="10" height="7" rx="1"/></svg><span>Tap Your Card on<br>Your Phone</span></div>
  <div class="item" style="left:17px;top:505px"><svg viewBox="0 0 17 17" fill="none" stroke="#fff" stroke-width="1"><rect x="4" y="1" width="9" height="15" rx="1.5"/><line x1="7" y1="13" x2="10" y2="13"/><rect x="6" y="4" width="5" height="6"/></svg><span>Hold your card near<br>the back of your<br>phone.</span></div>
  <div class="item" style="left:17px;top:549px"><svg viewBox="0 0 17 17" fill="none" stroke="#fff" stroke-width="1"><rect x="3" y="1" width="9" height="15" rx="1.5"/><circle cx="12" cy="11" r="4"/><path d="M10,11 l1.5,1.5 2.5,-3"/></svg><span>It will activate<br>automatically<br>no app needed.</span></div>
  <div class="item" style="left:17px;top:594px"><svg viewBox="0 0 17 17" fill="none" stroke="#fff" stroke-width="1"><rect x="3" y="1" width="9" height="15" rx="1.5"/><rect x="8" y="7" width="7" height="7" rx="1"/><line x1="8" y1="9" x2="15" y2="9"/></svg><span>The Bright Path<br>scheduler will open.</span></div>

  <div class="item" style="left:172px;top:473px"><svg viewBox="0 0 17 17" fill="none" stroke="#fff" stroke-width="1"><rect x="1" y="3" width="13" height="12" rx="1.5"/><line x1="1" y1="6.5" x2="14" y2="6.5"/><circle cx="12" cy="12" r="4" fill="var(--primary)"/><path d="M12,10 v2 h1.5"/></svg><span>Schedule Your<br>Appointment</span></div>
  <div class="item" style="left:172px;top:505px"><svg viewBox="0 0 17 17" fill="none" stroke="#fff" stroke-width="1"><rect x="1" y="1" width="6" height="6"/><rect x="9" y="1" width="6" height="6"/><rect x="1" y="9" width="6" height="6"/><path d="M10,8 l2,2 4,-5"/></svg><span>Select your clinical<br>concern.</span></div>
  <div class="item" style="left:172px;top:538px"><svg viewBox="0 0 17 17" fill="none" stroke="#fff" stroke-width="1"><rect x="1" y="2" width="14" height="12" rx="1"/><line x1="1" y1="5" x2="15" y2="5"/><circle cx="12" cy="12" r="3.5" fill="var(--primary)"/><path d="M12,10.5 v1.5 h1.2"/></svg><span>Choose your time<br>window.</span></div>
  <div class="item" style="left:172px;top:572px"><svg viewBox="0 0 17 17" fill="none" stroke="#fff" stroke-width="1"><rect x="1" y="2" width="13" height="14" rx="2"/><path d="M6,11 l8,-9 2,2 -8,9 -2.5,.5 Z"/></svg><span>Register (only once).</span></div>
  <div class="item" style="left:172px;top:593px"><svg viewBox="0 0 17 17" fill="none" stroke="#fff" stroke-width="1"><rect x="1" y="3" width="13" height="12" rx="1.5"/><line x1="4" y1="9" x2="8" y2="9"/><line x1="4" y1="12" x2="7" y2="12"/><circle cx="12.5" cy="11" r="2"/><path d="M9.5,16 a3,3 0 0 1 6,0"/></svg><span>Confirm your<br>appointment.</span></div>

  <div class="item" style="left:316px;top:473px"><svg viewBox="0 0 17 17" fill="none" stroke="#fff" stroke-width="1"><circle cx="9" cy="3.5" r="2.5"/><path d="M5,10 a4,4 0 0 1 8,0"/><path d="M1,13 h4 l3,2 h5 l3,-3"/></svg><span>Relax, we’ll take care<br>of the rest</span></div>
  <div class="item" style="left:316px;top:507px"><svg viewBox="0 0 17 17" fill="none" stroke="#fff" stroke-width="1"><rect x="1" y="3" width="13" height="12" rx="1.5"/><line x1="1" y1="6.5" x2="14" y2="6.5"/><circle cx="12" cy="12" r="4" fill="var(--primary)"/><path d="M10.5,10.5 q0,3 3,3"/></svg><span>A doctor will call during<br>your scheduled time.</span></div>
  <div class="item" style="left:316px;top:536px"><svg viewBox="0 0 17 17" fill="none" stroke="#fff" stroke-width="1"><rect x="7" y="1" width="9" height="13" rx="1.5"/><path d="M1,16 l3,-5 h4 l2,2"/><path d="M10,6 l1.5,1.5 2.5,-3"/></svg><span>Once booked, you’ll be<br>able to call our office.</span></div>
  <div class="item" style="left:316px;top:569px"><svg viewBox="0 0 17 17" fill="none" stroke="#fff" stroke-width="1"><rect x="1" y="4" width="15" height="10" rx="1"/><path d="M1,4 l7.5,6 7.5,-6"/><line x1="2" y1="1" x2="15" y2="16"/></svg><span>No emails, no texts<br>just a real person.</span></div>

  <div class="abs tagline">It’s that Simple</div>
</section>

<section class="flyer flyer--back">
  <svg class="flyer__shapes" viewBox="0 0 464 657" aria-hidden="true">
    <path fill="var(--sky)" d="M120,0 L464,0 L464,158 C180,165 50,230 0,347 C5,200 50,70 120,0 Z"/>
    <path fill="var(--accent)" d="M0,347 C50,225 170,150 464,131 L464,158 C180,165 50,230 0,347 Z"/>
    <path fill="var(--primary)" d="M255,657 C320,620 400,600 464,593 L464,657 Z"/>
  </svg>

  <h2 class="abs about">ABOUT <span class="about__name">Bright Path</span></h2>
  <p class="abs creator">Created by <b>Dr. Marcus Ferrigan</b></p>
  <p class="abs intro">Bright Path was founded to make healthcare simple and convenient.<br>Prescription renewals. Common infections. Medical notes. And so much more.</p>

  <p class="abs reach">Our doctors can address <span class="reach__big">120+</span> health concerns virtually<br>providing quality care without the waiting room.</p>
  <p class="abs promise"><span class="promise__accent">No waiting rooms.</span> Just real doctors providing real care.</p>

  <table class="benefits">
    <thead>
      <tr><th>Why Patients Choose<br>Bright Path</th><th>How It Works</th></tr>
    </thead>
    <tbody>
      <tr class="r1"><td class="left">Easy access</td><td>Book your visit</td></tr>
      <tr class="r2"><td class="left" rowspan="2">book and be seen from<br>anywhere in BC. Effortless booking</td><td>choose a time window that<br>fits your day.</td></tr>
      <tr class="r3"><td>Join the queue</td></tr>
      <tr class="r4"><td class="left">tap your Bright Path<br>Card to begin</td><td>you’ll be called when it’s your turn</td></tr>
      <tr class="r5"><td class="left">Trusted physicians</td><td>Speak directly with your doctor</td></tr>
      <tr class="r6"><td class="left">every visit is with a licensed<br>BC family doctor.</td><td>simple, secure, and stress-free.</td></tr>
    </tbody>
  </table>

  <div class="abs closing">Convenient Care for Common Concerns</div>
  <div class="abs thanks">
    <div class="thanks__title">THANK YOU!</div>
    <div class="thanks__url">http://brightpath-example.test/</div>
  </div>
</section>

</body>
</html>
```